Clear Harbor Tri-Fold Brochure - Recovering From Alzheimer's

Design a brochure a brochure for Clear Harbor. www.clearharborcare.example. We help people with Alzheimer's, or who have had a Traumatic Brain Injury, Concussion or Stroke stop their cognitive decline, and actually reverse decline and improve their cognitive abilities. We use an individualized approach, utilizing extensive lab work and developing a roadmap that includes diet, supplementation, theraputic devices all guided by a Memory Coach. I would like to see a design with pictures of people similar to the demographic on the website. Also incorporate some of the colors from my logo. We offer hope to people who consistently hear, "There is nothing we can do. Alzheimer's is a fatal disease." NOT TRUE! We see people's lives change every day!!!!

Target Market(s)

People who ARE or know someone suffering from cognitive decline, Alzheimer's, Traumatic Brain Injury, Concussion or Stroke.

Industry/Entity Type

Health and wellbeing -- Treating Alzheimer's.

Font styles to use
Other font styles liked:
• Calibri or I think it's called Lota

Colors
0054AA
0677BA
7BADD7
CADEEF
E8F1F8
0094D4
00A9DD
6FCCEA
C7EBF8
E9F6FB
00AB8E
00BBA5
67D7C9
C6EFE9
E9F9F6

Requirements
Must have
• Easily read material (think older eyes) and people between the ages of 40-70. Needs to have a professional feel but not clinical. Create trust and a feeling of caring and hope.
Nice to have
• Please check out my website: www.clearharborcare.example for content and feel.
Should not have
• Youthful people exercising OR highly stereotypical ageist photos or info.

```html
<!DOCTYPE html>
<html lang="en">
<head>
<meta charset="utf-8">
<title>Clear Harbor Tri-Fold Brochure</title>
<link href="https://fonts.googleapis.com/css2?family=Lato:ital,wght@0,400;0,700;0,900;1,400&family=Cinzel:wght@700&display=swap" rel="stylesheet">
<style>
  :root{
    --navy:#0d4a8c;
    --navy-deep:#0a3d78;
    --blue:#0677BA;
    --green:#4caf3f;
    --green-dark:#2f8f3a;
    --ink:#2c3440;
    --muted:#5b6673;
    --paper:#ffffff;
    --bg:#e6e7e8;
    --photo-warm:#b89a74;
    --photo-cool:#8ea7b8;
  }
  *{box-sizing:border-box;margin:0;padding:0}
  html,body{width:1200px;height:2390px;overflow:hidden;background:var(--bg)}
  body{position:relative;font-family:"Lato",Arial,sans-serif;color:var(--ink)}
  .spread{position:absolute;left:40px;width:1120px;height:866px;display:flex;box-shadow:0 6px 24px rgba(0,0,0,.18);background:var(--paper)}
  .spread--outside{top:200px}
  .spread--inside{top:1324px}
  .panel{position:relative;width:373.33px;height:100%;overflow:hidden}
  .panel--white{background:var(--paper)}
  .panel--blue{background:var(--navy);color:#fff}
  .photo{position:absolute;left:0;width:100%}
  .curves{position:absolute;inset:0;width:100%;height:100%;pointer-events:none}
  .content{position:absolute;left:30px;right:30px}
  h2,h3{font-family:"Lato",Arial,sans-serif}
  .eyebrow{color:var(--green-dark);font-weight:900;font-size:15px;letter-spacing:.04em;text-transform:uppercase;line-height:1.3}
  .sub{color:var(--navy);font-weight:700;font-size:15px;margin:10px 0 6px}
  .body-text{font-size:12.5px;line-height:1.55;color:var(--muted)}
  .panel--blue .body-text{color:#dfe9f5}
  .ticks{list-style:none;margin-top:4px}
  .ticks li{position:relative;padding-left:16px;font-size:12.5px;line-height:1.7;color:var(--muted)}
  .ticks li::before{content:"";position:absolute;left:0;top:7px;width:8px;height:8px;border-radius:50%;background:var(--green)}
  .brand{display:flex;align-items:center;gap:10px;font-family:"Lato",Arial,sans-serif;font-weight:900;color:var(--navy);font-size:24px;letter-spacing:.04em;text-transform:uppercase}
  .brand-dot{width:34px;height:34px;border-radius:50%;background:var(--green)}
  .pill{display:block;background:var(--green);color:#fff;font-weight:700;font-size:16px;text-align:center;border-radius:22px;padding:9px 10px}
  .cover-title{font-weight:900;font-size:30px;line-height:1.12;color:#fff;text-transform:uppercase;letter-spacing:.02em}
  .cta-box{border:2px solid var(--green);border-radius:10px;padding:12px 14px;text-align:center;font-weight:700;font-size:16px;line-height:1.4}
  .phone{display:inline-flex;align-items:center;gap:6px;font-weight:900}
  .socials{display:flex;gap:10px;justify-content:center}
  .socials span{width:22px;height:22px;border-radius:50%;background:var(--green)}
  .service{display:flex;gap:12px;margin-bottom:16px}
  .service-icon{flex:0 0 34px;height:34px;border-radius:50%;border:2px solid var(--green);display:flex;align-items:center;justify-content:center}
  .service-icon span{width:12px;height:12px;border-radius:50%;background:var(--green)}
  .service h3{color:#8fd37e;font-size:14px;font-weight:900;text-transform:uppercase;letter-spacing:.03em;margin-bottom:3px}
  .quote-box{border:2px solid var(--green);border-radius:10px;padding:10px 12px;text-align:center;font-style:italic;color:var(--green-dark);font-size:14px;line-height:1.4}
  .rule{height:2px;background:var(--green);width:60px;margin:6px 0 8px}
</style>
</head>
<body>

<!-- Outside spread: inside flap, back panel, front cover -->
<section class="spread spread--outside">

  <article class="panel panel--white">
    <div class="photo" style="top:0;height:250px;background:linear-gradient(135deg,var(--photo-cool),var(--photo-warm))" role="img" aria-label="Photo of an older couple smiling together outdoors"></div>
    <svg class="curves" viewBox="0 0 373 866" preserveAspectRatio="none">
      <path d="M0 250 Q190 200 373 215 L373 0 L373 0" fill="none"/>
      <path d="M0 262 Q190 208 373 220 L373 232 Q190 224 0 280 Z" fill="var(--paper)"/>
      <path d="M0 262 Q190 208 373 220" stroke="var(--navy)" stroke-width="5" fill="none"/>
      <path d="M0 800 Q190 760 373 790 L373 866 L0 866 Z" fill="var(--green)"/>
      <path d="M0 812 Q190 776 373 804 L373 866 L0 866 Z" fill="var(--navy)"/>
    </svg>
    <div class="content" style="top:300px">
      <p class="eyebrow">Taking care of your brain should not be a mystery</p>
      <p class="sub">Have You Noticed?</p>
      <ul class="ticks">
        <li>Brain fog most days</li>
        <li>Losing track of words or names</li>
        <li>Trouble focusing on simple tasks</li>
        <li>Feeling lost in familiar places</li>
        <li>Forgetting recent conversations</li>
        <li>Changes in mood or sleep</li>
      </ul>
      <p class="sub" style="color:var(--green-dark);font-style:italic;text-align:center;margin-top:14px">Cognitive decline is not inevitable<br>at any age</p>
      <p class="body-text" style="text-align:center">For over a decade we have helped people take back their memory, focus and joy through a plan built for them.</p>
    </div>
    <p style="position:absolute;left:0;right:0;bottom:20px;text-align:center;color:#fff;font-weight:700;font-size:15px">www.clearharborcare.example</p>
  </article>

  <article class="panel panel--blue">
    <svg class="curves" viewBox="0 0 373 866" preserveAspectRatio="none">
      <path d="M0 780 Q190 740 373 770 L373 866 L0 866 Z" fill="var(--green)"/>
      <path d="M0 794 Q190 758 373 786 L373 866 L0 866 Z" fill="var(--paper)"/>
    </svg>
    <div style="position:absolute;left:116px;top:30px;width:142px;height:142px;border-radius:50%;border:6px solid var(--green);background:linear-gradient(135deg,var(--photo-warm),#9fb58a)" role="img" aria-label="Circular photo of an older woman gardening with flowers"></div>
    <div class="content" style="top:196px;text-align:center">
      <p style="font-family:'Lato',Arial,sans-serif;font-weight:900;font-size:24px;letter-spacing:.05em;text-transform:uppercase">Clear Harbor</p>
      <p class="body-text" style="font-size:14px;margin-top:12px">We offer hope to people who consistently hear, “There is nothing we can do. Alzheimer’s is a fatal disease.”</p>
      <p style="font-weight:900;font-size:16px;margin-top:12px;color:#8fd37e">NOT TRUE! We see people’s lives change every day!!</p>
      <p style="font-weight:900;font-size:19px;margin-top:22px;text-transform:uppercase;line-height:1.25">Join the Brain<br>Health Revolution!</p>
      <div class="cta-box" style="margin-top:22px">Call us now for your free consultation:
        <span class="phone"><svg width="16" height="16" viewBox="0 0 24 24"><path fill="#8fd37e" d="M6.6 10.8a15 15 0 0 0 6.6 6.6l2.2-2.2a1 1 0 0 1 1-.25 11.4 11.4 0 0 0 3.6.57 1 1 0 0 1 1 1V20a1 1 0 0 1-1 1A17 17 0 0 1 3 4a1 1 0 0 1 1-1h3.5a1 1 0 0 1 1 1c0 1.25.2 2.45.57 3.6a1 1 0 0 1-.25 1z"/></svg>555-014-2290</span>
      </div>
      <p class="body-text" style="margin-top:26px;font-size:13px;line-height:1.7">Harbor Street, Lakeview<br>555-010-7890<br>hello@clearharborcare.example</p>
      <div class="socials" style="margin-top:16px"><span></span><span></span><span></span><span></span></div>
    </div>
  </article>

  <article class="panel panel--white">
    <div style="position:absolute;left:0;right:0;top:40px;display:flex;justify-content:center">
      <div class="brand"><span class="brand-dot"></span>Clear Harbor</div>
    </div>
    <div class="photo" style="top:130px;height:560px;background:linear-gradient(160deg,#d9c39c,var(--photo-warm) 55%,#7d8a5a)" role="img" aria-label="Photo of grandparents laughing outdoors with a young granddaughter on the grandfather's shoulders"></div>
    <svg class="curves" viewBox="0 0 373 866" preserveAspectRatio="none">
      <path d="M0 130 L0 168 Q190 110 373 100 L373 130 Z" fill="none"/>
      <path d="M0 120 L373 120 L373 90 Q190 100 0 165 Z" fill="var(--paper)"/>
      <path d="M0 165 Q190 100 373 90" stroke="var(--navy)" stroke-width="5" fill="none"/>
      <path d="M0 0 L373 0 L373 92 Q190 102 0 163 Z" fill="var(--paper)"/>
      <path d="M0 660 Q190 600 373 560 L373 866 L0 866 Z" fill="var(--green)"/>
      <path d="M0 676 Q190 620 373 580 L373 866 L0 866 Z" fill="var(--navy)"/>
    </svg>
    <div class="content" style="top:700px;text-align:center">
      <h1 class="cover-title">You Can Change<br>Your Brain Health</h1>
      <span class="pill" style="margin-top:22px;font-size:14px">www.clearharborcare.example</span>
    </div>
  </article>
</section>

<!-- Inside spread: philosophy, services, call to action -->
<section class="spread spread--inside">

  <article class="panel panel--white">
    <div class="content" style="top:36px">
      <h2 class="eyebrow" style="color:var(--navy);font-size:17px">Our Philosophy</h2>
      <div class="rule"></div>
      <p class="body-text">You may believe there is nothing you can do to prevent or treat cognitive decline and Alzheimer’s disease. Maybe the idea of a personalized plan to prevent or reverse decline sounds too simple. We build a plan around you, using lab work, nutrition and daily habits to support lasting brain health.</p>
      <p class="eyebrow" style="margin-top:12px;font-size:14px">Yes! Your brain can change!</p>
      <p class="sub" style="margin-top:16px">First Steps</p>
      <p class="body-text">The first step is your free 30 minute consultation to learn more about Clear Harbor and our services.</p>
      <p class="body-text" style="margin-top:8px">Maintaining brain clarity, easing brain fog and reclaiming cognitive decline is a journey, and a guided plan makes every step simpler.</p>
      <p class="eyebrow" style="margin-top:18px;text-align:center;font-size:15px">Schedule Your Appointment</p>
      <p style="text-align:center;margin-top:6px;color:var(--green-dark);font-size:17px" class="phone">
        <svg width="18" height="18" viewBox="0 0 24 24"><path fill="var(--green)" d="M6.6 10.8a15 15 0 0 0 6.6 6.6l2.2-2.2a1 1 0 0 1 1-.25 11.4 11.4 0 0 0 3.6.57 1 1 0 0 1 1 1V20a1 1 0 0 1-1 1A17 17 0 0 1 3 4a1 1 0 0 1 1-1h3.5a1 1 0 0 1 1 1c0 1.25.2 2.45.57 3.6a1 1 0 0 1-.25 1z"/></svg>555-014-2290</p>
    </div>
    <div class="photo" style="top:600px;height:266px;background:linear-gradient(135deg,#7fa36a,var(--photo-warm))" role="img" aria-label="Photo of a grandfather and grandson smiling together on the grass"></div>
    <svg class="curves" viewBox="0 0 373 866" preserveAspectRatio="none">
      <path d="M0 600 L373 600 L373 640 Q190 600 0 630 Z" fill="var(--paper)"/>
      <path d="M0 630 Q190 600 373 640" stroke="var(--navy)" stroke-width="5" fill="none"/>
    </svg>
  </article>

  <article class="panel panel--blue">
    <svg class="curves" viewBox="0 0 373 866" preserveAspectRatio="none">
      <path d="M0 0 L373 0 L373 40 Q190 20 0 60 Z" fill="var(--navy-deep)"/>
    </svg>
    <p style="position:absolute;top:18px;left:0;right:0;text-align:center;font-weight:900;letter-spacing:.08em;font-size:14px">OUR SERVICES</p>
    <div class="content" style="top:78px">
      <div class="service"><div class="service-icon"><span></span></div><div><h3>Personal Services</h3><p class="body-text">Our approach is personal. We start with detailed lab work and a full history, then design a roadmap of diet, supplements and daily habits.</p></div></div>
      <div class="service"><div class="service-icon"><span></span></div><div><h3>Remote Services</h3><p class="body-text">We work with you wherever you live. Calls and online check-ins keep your plan on track with your Memory Coach.</p></div></div>
      <div class="service"><div class="service-icon"><span></span></div><div><h3>Customized Options</h3><p class="body-text">Time and money matter. Choose a level of support that fits your needs, from guided coaching to full programs.</p></div></div>
      <div class="service"><div class="service-icon"><span></span></div><div><h3>Brain Studio</h3><p class="body-text">Do you need a gym for your brain? Our studio offers therapeutic devices and guided sessions to help strengthen focus and memory.</p></div></div>
    </div>
    <div class="content" style="bottom:34px"><span class="pill" style="font-size:14px">www.clearharborcare.example</span></div>
  </article>

  <article class="panel panel--white">
    <div class="photo" style="top:0;height:230px;background:linear-gradient(135deg,#a9b7c6,var(--photo-warm) 60%,#b0663f)" role="img" aria-label="Photo of a group of older friends walking and laughing together outdoors"></div>
    <svg class="curves" viewBox="0 0 373 866" preserveAspectRatio="none">
      <path d="M0 230 Q190 190 373 160 L373 866 L0 866 Z" fill="var(--paper)"/>
      <path d="M0 230 Q190 190 373 160" stroke="var(--navy)" stroke-width="5" fill="none"/>
    </svg>
    <div class="content" style="top:256px">
      <h2 class="eyebrow" style="font-size:16px">Join the Brain<br>Health Revolution!</h2>
      <ul class="ticks" style="margin-top:10px">
        <li>Enhance Brain Function</li>
        <li>Optimize your brain at any age</li>
        <li>Do not settle</li>
        <li>Prevent Cognitive Decline</li>
        <li>Reverse Early Dementia</li>
      </ul>
      <p style="color:var(--green-dark);font-weight:700;font-size:14px;margin-top:14px">Proven strategies can change your life and destiny.</p>
      <div class="quote-box" style="margin-top:20px">“You are not alone...this is not the end of your story.”</div>
      <p class="eyebrow" style="color:var(--navy);margin-top:24px">Clear Harbor<br>for better brain health</p>
      <p class="body-text" style="margin-top:6px">Start your journey today with your FREE 30 minute consultation. Our caring team will help you take control of your brain health and your future.</p>
    </div>
  </article>
</section>

</body>
</html>
```